Music producer seeks album cover!

Hi there designers. I need a design for my new album - the CD cover, CD itself and the album artwork for Tunevale and other streaming sites. This is my 'Salt and Ember' album: it's about gender and sexuality, and not conforming to labels. Musically it combines the pink of disco with the purple of rock.

The front cover should only be visuals and 'rowena dask' in all lower case with no capitals, and no album title, just a design in Salt and Ember please. I'd like to see something very simple, bold and iconic. For inspiration, how about jellyfish, squid, orca or zebra? All in Salt and Ember of course :-) Or how about the male and female parts of a flower, stamen and pistil?

For the back cover, I have quite a bit of text, attached as a word file.

The CD artwork and album artwork for streaming sites should be versions of the front cover. I will attach a template for the print-ready artwork . The streaming artwork needs to be a perfect square JPG or PNG, at least 4000 x 4000 pixels. It doesn't need the artist name.

```html
<!DOCTYPE html>
<html lang="en">
<head>
<meta charset="utf-8">
<title>rowena dask — Salt and Ember</title>
<link rel="stylesheet" href="https://fonts.googleapis.com/css2?family=Inter:wght@300;400;600;700&family=Bodoni+Moda:wght@400&display=swap">
<style>
  :root {
    --ink-deep: #140a2a;
    --white: #ffffff;
    --pink: #e4589f;
    --lavender: #a986dc;
    --leader: rgba(255,255,255,0.55);
  }
  * { margin: 0; padding: 0; box-sizing: border-box; }
  html, body { width: 1200px; height: 600px; overflow: hidden; background: var(--ink-deep); }
  body { font-family: "Inter", Helvetica, Arial, sans-serif; color: var(--white); }

  .spread { position: relative; width: 1200px; height: 600px; display: flex; }
  .back-cover, .front-cover { position: relative; width: 600px; height: 600px; overflow: hidden; }

  .back-photo {
    position: absolute; inset: 0;
    background:
      radial-gradient(ellipse 130px 200px at 400px 330px, rgba(160,30,60,0.85), transparent 70%),
      radial-gradient(ellipse 220px 140px at 140px 420px, rgba(170,60,200,0.55), transparent 70%),
      radial-gradient(ellipse 260px 160px at 120px 140px, rgba(80,50,170,0.6), transparent 70%),
      radial-gradient(ellipse 200px 260px at 520px 120px, rgba(20,10,30,0.9), transparent 70%),
      linear-gradient(160deg, #2a1c6a 0%, #1a1040 45%, #2c1a62 100%);
  }
  .front-photo {
    position: absolute; inset: 0;
    background:
      radial-gradient(ellipse 150px 130px at 330px 250px, rgba(240,170,240,0.85), transparent 70%),
      radial-gradient(ellipse 110px 90px at 190px 300px, rgba(210,40,70,0.8), transparent 70%),
      radial-gradient(ellipse 240px 200px at 320px 230px, rgba(170,70,200,0.75), transparent 72%),
      radial-gradient(ellipse 180px 160px at 320px 460px, rgba(150,60,190,0.5), transparent 70%),
      linear-gradient(150deg, #2a1a60 0%, #3a2580 50%, #2a1f6a 100%);
  }

  .tracklist {
    position: absolute; left: 28px; top: 36px;
    font-weight: 700; font-size: 25px; line-height: 23.2px; letter-spacing: -0.2px;
    list-style: none; white-space: nowrap;
  }
  .tracklist .pink { color: var(--pink); }
  .tracklist .lav { color: var(--lavender); }

  .album-note {
    position: absolute; right: 27px; top: 46px;
    text-align: right; font-weight: 400; font-size: 11.5px; line-height: 10px;
  }
  .album-note .pink { color: var(--pink); }
  .album-note .lav { color: var(--lavender); }

  .spaced {
    position: absolute; left: 28px; width: 548px;
    font-size: 9px; text-align: justify; text-align-last: justify; white-space: nowrap;
  }
  .featuring { top: 299px; }
  .mastering { top: 508px; }
  .mastering b { font-weight: 700; }

  .musicians {
    position: absolute; left: 28px; top: 316px; width: 548px;
    list-style: none; font-size: 8.3px; line-height: 9.1px;
  }
  .musicians li { display: flex; align-items: baseline; height: 9.1px; }
  .musicians .name { font-weight: 700; white-space: nowrap; }
  .musicians .leader { flex: 1; border-bottom: 1px dashed var(--leader); margin: 0 3px; transform: translateY(-2px); }
  .musicians .role { white-space: nowrap; font-weight: 400; }

  .thanks {
    position: absolute; left: 28px; top: 527px; width: 548px;
    font-size: 8.1px; line-height: 9.1px; text-align: justify;
  }
  .signoff { position: absolute; right: 24px; top: 554px; font-size: 8.1px; }
  .website { position: absolute; right: 24px; top: 571px; font-size: 9.5px; font-weight: 700; color: var(--pink); }

  .artist-name {
    position: absolute; left: 629px; width: 542px; top: 552px;
    display: flex; justify-content: space-between;
    font-family: "Bodoni Moda", "Didot", serif; font-size: 24px; font-weight: 400;
  }
  .artist-name .gap { width: 26px; }
</style>
</head>
<body>
<main class="spread">
  <section class="back-cover">
    <div class="back-photo" role="img" aria-label="Photograph of a glowing jellyfish with red bell and violet tentacles drifting in dark water"></div>

    <ol class="tracklist">
      <li><span class="pink">marlow</span></li>
      <li><span class="lav">velvet</span> lighthouse</li>
      <li>honey <span class="pink">static</span></li>
      <li>berlin <span class="lav">kept</span> my heart</li>
      <li>was it the <span class="lav">late tram?</span></li>
      <li><span class="lav">meridale</span></li>
      <li>oakhollow lane</li>
      <li><span class="pink">ghosts</span></li>
      <li>borrowed <span class="lav">mirrors</span></li>
      <li><span class="pink">farewell</span> darling</li>
    </ol>

    <p class="album-note">
      Rowena<br>Dask’s<br><span class="lav">Salt</span><br>and<br><span class="pink">Ember</span><br>album was<br>written and<br>produced by<br>Rowena<br>Dask;<br>spoken<br>word<br>on ‘marlow’<br>written by<br>Owen Larch;<br>string<br>arrangement<br>for ‘berlin<br>kept<br>my heart’<br>written by<br>Ned Fallow
    </p>

    <p class="spaced featuring">F e a t u r i n g ,&nbsp; i n &nbsp;o r d e r &nbsp;o f &nbsp;a p p e a r a n c e :</p>

    <ul class="musicians">
      <li><span class="name">Owen Larch</span><span class="leader"></span><span class="role">spoken word, track 1</span></li>
      <li><span class="name">Jonah Greer (via Sessionwell)</span><span class="leader"></span><span class="role">organ on track 1, electric piano on track 8</span></li>
      <li><span class="name">Rowena Dask</span><span class="leader"></span><span class="role">vocals, guitars, bass guitar, keyboards, sampler</span></li>
      <li><span class="name">Colin Barrow (via Sessionwell)</span><span class="leader"></span><span class="role">drums, tracks 1 and 2</span></li>
      <li><span class="name">Aurelie Marthe Beaulac</span><span class="leader"></span><span class="role">saxophones, tracks 1, 3, 9</span></li>
      <li><span class="name">Rosa Anders</span><span class="leader"></span><span class="role">vocals, track 2</span></li>
      <li><span class="name">Velvet Echo (via Sessionwell)</span><span class="leader"></span><span class="role">vocals, tracks 2, 4, 5, 6, 7, 8, 10</span></li>
      <li><span class="name">Dev Bekker</span><span class="leader"></span><span class="role">organ, track 2</span></li>
      <li><span class="name">Tamsin Dask</span><span class="leader"></span><span class="role">guitar solo, track 2</span></li>
      <li><span class="name">Dario Mulroy (via Sessionwell)</span><span class="leader"></span><span class="role">beat programming, track 3</span></li>
      <li><span class="name">Matteo Crevani (via Sessionwell)</span><span class="leader"></span><span class="role">piano, track 4</span></li>
      <li><span class="name">Lucy Marr</span><span class="leader"></span><span class="role">vocals, track 4</span></li>
      <li><span class="name">Luca Lozano Ibarra</span><span class="leader"></span><span class="role">violins, track 4</span></li>
      <li><span class="name">Jude Zeller (via Sessionwell)</span><span class="leader"></span><span class="role">cello, track 4</span></li>
      <li><span class="name">Aaron Aveni (via Sessionwell)</span><span class="leader"></span><span class="role">drums, tracks 4, 5, 6, 7, 8, 9, 10</span></li>
      <li><span class="name">Elodie Hartigan</span><span class="leader"></span><span class="role">spoken word, tracks 5, 7, 10</span></li>
      <li><span class="name">Linnea (via Sessionwell)</span><span class="leader"></span><span class="role">vocals, tracks 6 and 8</span></li>
      <li><span class="name">Tobias Hale</span><span class="leader"></span><span class="role">spoken word, track 7</span></li>
      <li><span class="name">Drew Kestle</span><span class="leader"></span><span class="role">vocals, tracks 7 and 10</span></li>
      <li><span class="name">Jack Zennor</span><span class="leader"></span><span class="role">vocals, track 9</span></li>
    </ul>

    <p class="spaced mastering">M a s t e r e d &nbsp;b y &nbsp;<b>M i l e s &nbsp;A s h c o m b e</b> &nbsp;a t &nbsp;<b>V E G A</b></p>

    <p class="thanks">Huge thanks to the team at Sessionwell, to all the amazing musicians who put their soul into this record, and to my family and friends who continue to inspire, support and encourage me in my music. Peace and love to the female and the male, the binary and the non-binary, the conformers and the non-conformers, the salt and the ember.</p>
    <p class="signoff">- Rowena Dask, 2023</p>
    <p class="website">openairsound.com</p>
  </section>

  <section class="front-cover">
    <div class="front-photo" role="img" aria-label="Photograph of a large pink and violet jellyfish glowing against deep purple water"></div>
  </section>

  <h1 class="artist-name" aria-label="rowena dask">
    <span>r</span><span>o</span><span>w</span><span>e</span><span>n</span><span>a</span><span class="gap"></span><span>d</span><span>a</span><span>s</span><span>k</span>
  </h1>
</main>
</body>
</html>
```